Zielgruppe
Wir sind ein Reisebüro (online und offline) mit dem Schwerpunkt Pauschalflugreisen, individuelle Flugreisen sowie Kreuzfahrten. Unsere Zielgruppe ist bunt gemischt, eher aber mit etwas gehobeneren, der heutigen Zeit entsprechenden Ansprüchen. Es sind Kunden, die mehr Wert auf qualifizierte Beratung legen und nicht auf der "geiz ist geil" Schiene fahren.
Aufgabenstellung
Wir benötigen Briefpapier, Visitenkarten, Katalogaufkleber und Stempel mit typischen Angaben, auf dem Briefpapier inkl. der Bankverbindung.

```html
<!DOCTYPE html>
<html lang="de">
<head>
<meta charset="utf-8">
<title>Fernkompass.de – Briefpapier</title>
<link rel="stylesheet" href="https://fonts.googleapis.com/css2?family=Exo+2:ital,wght@0,600;1,500;1,600;1,700&display=swap">
<style>
  :root {
    --stage: #82bad9;
    --paper: #f8fbfb;
    --navy: #0a1a33;
    --navy-mid: #0c2e50;
    --brand-blue: #1a7bbd;
    --sky: #2ab4e6;
    --date-blue: #5aa0cc;
    --ink: #0f1d3a;
    --ghost: #efefef;
  }
  * { margin: 0; padding: 0; box-sizing: border-box; }
  html, body { width: 928px; height: 1200px; overflow: hidden; }
  body {
    background: var(--stage);
    font-family: "Exo 2", "Trebuchet MS", sans-serif;
    position: relative;
  }
  .letterhead {
    position: absolute;
    left: 86px; top: 111px;
    width: 754px; height: 975px;
    background: var(--paper);
    overflow: hidden;
  }
  .header-band, .footer-band { position: absolute; left: 0; top: 0; }
  .brand-name {
    position: absolute; left: 42px; top: 46px;
    font-size: 31px; font-weight: 600; color: #ffffff;
    letter-spacing: -0.3px;
  }
  .brand-dot {
    position: absolute; left: 68px; top: 30px;
    width: 12px; height: 12px; border-radius: 50%;
    background: var(--sky);
  }
  .brand-url {
    position: absolute; left: 82px; top: 92px;
    font-size: 19px; font-style: italic; font-weight: 600;
    color: #3a8fcf;
  }
  .recipient { position: absolute; left: 47px; top: 218px; }
  .recipient-name {
    font-size: 23px; font-style: italic; font-weight: 700;
    color: var(--brand-blue);
    margin-bottom: 4px;
  }
  .recipient-address {
    font-size: 16px; font-style: italic; font-weight: 600;
    color: var(--ink); line-height: 19px;
  }
  .letter-date {
    position: absolute; left: 47px; top: 347px;
    font-size: 17px; font-style: italic; font-weight: 600;
    color: var(--date-blue);
  }
  .ghost-mark {
    position: absolute; left: 70px; top: 520px;
    font-size: 96px; font-weight: 600; color: var(--ghost);
    transform: rotate(-22deg); transform-origin: left top;
    white-space: nowrap; opacity: 0.75;
  }
  .contact-list {
    position: absolute; left: 39px; top: 882px;
    list-style: none;
  }
  .contact-item {
    display: flex; align-items: center; gap: 11px;
    height: 24px;
    font-size: 12.5px; font-weight: 600; color: var(--ink);
    letter-spacing: 0.6px;
  }
  .contact-item.email { font-style: italic; font-size: 13.5px; letter-spacing: 0; }
  .contact-icon { width: 20px; height: 16px; fill: #1d5a96; flex: none; }
</style>
</head>
<body>
  <main class="letterhead">
    <svg class="header-band" width="754" height="210" viewBox="0 0 754 210" aria-hidden="true">
      <defs>
        <linearGradient id="headerFill" x1="0" y1="0" x2="1" y2="0">
          <stop offset="0" stop-color="#0a1428"/>
          <stop offset="0.6" stop-color="#0a2748"/>
          <stop offset="1" stop-color="#0d3a60"/>
        </linearGradient>
        <linearGradient id="streak" x1="0" y1="0" x2="1" y2="0">
          <stop offset="0" stop-color="#8fb9cf" stop-opacity="0"/>
          <stop offset="0.5" stop-color="#7fc0dc"/>
          <stop offset="1" stop-color="#2ab4e6"/>
        </linearGradient>
      </defs>
      <path d="M0 0 H730 C600 80 440 120 330 138 C200 158 60 175 0 201 Z" fill="url(#headerFill)"/>
      <path d="M180 165 C300 140 420 125 500 100 C600 70 680 30 754 0 L754 6 C680 40 600 80 500 110 C420 130 300 150 180 165 Z" fill="url(#streak)"/>
      <path d="M360 136 C460 120 560 95 640 60 C690 38 730 18 754 4" stroke="#2ab4e6" stroke-width="3" fill="none"/>
    </svg>

    <span class="brand-dot"></span>
    <div class="brand-name">Fernkompass.de</div>
    <div class="brand-url">www.fernkompass.de</div>

    <div class="ghost-mark" aria-hidden="true">Fernkompass.de</div>

    <section class="recipient">
      <div class="recipient-name">Brandauer &amp; Kessling</div>
      <div class="recipient-address">Lindenhofweg 8<br>D–65183 Wiesbaden</div>
    </section>

    <div class="letter-date">21 August 2013</div>

    <ul class="contact-list">
      <li class="contact-item">
        <svg class="contact-icon" viewBox="0 0 20 16" aria-hidden="true"><path d="M1 5 C4 1 16 1 19 5 L16 7 L14 5 H6 L4 7 Z"/><rect x="4" y="7" width="12" height="8" rx="1"/></svg>
        <span>+49(0)611 – 482930</span>
      </li>
      <li class="contact-item">
        <svg class="contact-icon" viewBox="0 0 20 16" aria-hidden="true"><rect x="6" y="0" width="7" height="6"/><rect x="1" y="6" width="18" height="6" rx="1"/><rect x="1" y="13" width="18" height="3"/></svg>
        <span>+49(0)611 – 7315526</span>
      </li>
      <li class="contact-item email">
        <svg class="contact-icon" viewBox="0 0 20 16" aria-hidden="true"><path d="M1 2 H19 L10 9 Z"/><path d="M1 4 L10 11 L19 4 V15 H1 Z"/></svg>
        <span>service@fernkompass.de</span>
      </li>
    </ul>

    <svg class="footer-band" width="754" height="975" viewBox="0 0 754 975" aria-hidden="true" style="pointer-events:none">
      <defs>
        <linearGradient id="footerFill" x1="0" y1="0" x2="1" y2="0">
          <stop offset="0" stop-color="#0b2140"/>
          <stop offset="1" stop-color="#0d3458"/>
        </linearGradient>
      </defs>
      <path d="M468 975 C560 930 660 890 754 874 V975 Z" fill="url(#footerFill)"/>
      <path d="M468 975 C560 925 660 880 754 864 L754 872 C660 890 560 932 480 975 Z" fill="#2ab4e6"/>
      <path d="M500 975 C580 938 670 900 754 882" stroke="#8fbfd6" stroke-width="2" fill="none"/>
    </svg>
  </main>
</body>
</html>
```